QV - menu design

Hi,

We require elegant menu design for upscale restaurant. Please find attached the logo and the menu items for your reference.

for inspiration, this is a good website: -
http://www.platewhisper.example/bellfoldnotes/about.php

We are very much open for Menu Size suggestions.

unfortunately the place is going under renovation, we don't have updated images to it. the closest look and feel to our place is http://varnelo.example ..

we are also open for creative options on the shape, the styles, etc. as long as it represents the fine dine feel ...

Thanks ...

Dear All,

We wouldlike to extend our apology for not being able to provide feedbacks on everysingle design. We were extremely busy and we have multiple contests opensimultaneously which makes the process even harder.

However,we would like to thank you all for the efforts you have put into designingour menu. It is very much appreciated …

We wishyou all success in your design ventures and we are quite positive that we willbe working with many of you on many projects in the soon future. 

Thanks & Regards,

TLG Team...

 

 

 

Industry/Entity Type

Restaurant

Requirements
Must have
• Please ensure that there are 'some' images in the menu ... this is very important.
Should not have
• IMPORTANT: -

1. Please DO NOT insert any currency sign to the menu
2. Please keep the prices of the menu at the end of the menu items descriptions NOT beside the menu item names. The font of the price should be similar to the menu item description and please DO NOT bold the numbers. the prices should be subtle.

Thank you ...

```html
<!DOCTYPE html>
<html lang="en">
<head>
<meta charset="utf-8">
<title>QV Café Menu</title>
<link href="https://fonts.googleapis.com/css2?family=Questrial&family=Didact+Gothic&display=swap" rel="stylesheet">
<style>
:root{
  --page:#ffffff;
  --black:#000000;
  --slate:#4b4b4d;
  --bronze:#a68a64;
  --gold:#e9b042;
  --ink:#ffffff;
  --cafe:#b08d5c;
}
*{margin:0;padding:0;box-sizing:border-box}
html,body{width:784px;height:1200px;overflow:hidden;background:var(--page)}
body{position:relative;font-family:"Didact Gothic","Questrial",sans-serif;color:var(--ink)}
.cover{position:absolute;top:8px;height:383px;background:var(--black)}
.cover-back{left:8px;width:378px}
.cover-front{left:392px;width:385px}
.brand{position:absolute;text-align:center;font-family:"Questrial",sans-serif;color:var(--ink)}
.brand-name{display:block;font-size:30px;letter-spacing:6px;line-height:1}
.brand-sub{display:block;font-size:9px;letter-spacing:5px;color:var(--cafe);margin-top:6px;text-align:right}
.cover-back .brand{left:92px;top:290px;width:200px}
.cover-front .brand{left:78px;top:160px;width:230px}
.menu-tab{position:absolute;left:155px;bottom:0;width:73px;height:34px;background:var(--bronze);font-family:"Questrial",sans-serif;font-size:19px;color:var(--ink);text-align:center;line-height:36px}
.spread{position:absolute;left:10px;width:767px;height:385px;background:var(--slate)}
.spread-one{top:407px}
.spread-two{top:806px}
.photo{position:absolute;top:0;height:100%}
.photo-left{left:0;width:118px;border-right:3px solid var(--bronze)}
.photo-right{right:0;width:116px;border-left:3px solid var(--bronze)}
.ph-breakfast{background:linear-gradient(160deg,#e8a23a 0%,#c9742a 35%,#f3e7b0 60%,#f6d66a 80%,#7aa14a 100%)}
.ph-sandwich{background:linear-gradient(170deg,#c2272b 0%,#d9a767 30%,#8fb04a 55%,#c9963f 75%,#3a2a20 100%)}
.ph-salad{background:linear-gradient(150deg,#1f4e1f 0%,#6f9b36 35%,#d7243a 55%,#b7c85a 75%,#2e5a25 100%)}
.ph-club{background:linear-gradient(170deg,#d6d2c4 0%,#c9a872 30%,#c23a2e 50%,#9fbf5a 70%,#e9ddc2 100%)}
.column{position:absolute;top:22px}
.col-a{left:132px;width:237px}
.col-b{left:396px;width:230px}
h2{font-family:"Questrial",sans-serif;font-weight:400;font-size:17px;color:var(--ink);margin-bottom:14px}
h2.later{margin-top:16px;margin-bottom:10px}
.item{margin-bottom:7px;font-size:7.6px;line-height:8.6px;text-align:justify}
.item-name{display:block;color:var(--gold);font-weight:700;font-size:9.4px;line-height:11px}
.inline-name{color:var(--gold);font-weight:700}
.price{color:var(--gold)}
.col-b .item{margin-bottom:9px}
.col-b .item-name{font-size:8.6px;line-height:10px}
</style>
</head>
<body>

<section class="cover cover-back">
  <div class="brand"><span class="brand-name">QUILL VALE</span><span class="brand-sub">CAFÉ</span></div>
</section>
<section class="cover cover-front">
  <div class="brand"><span class="brand-name">QUILL VALE</span><span class="brand-sub">CAFÉ</span></div>
  <div class="menu-tab">MENU</div>
</section>

<section class="spread spread-one">
  <div class="photo photo-left ph-breakfast" role="img" aria-label="Photo of toast, orange juice and scrambled eggs with basil"></div>
  <div class="column col-a">
    <h2>The Breakfast</h2>
    <p class="item"><span class="item-name">Butter Croissant</span>Served plain with a selection of two jams, a vanilla custard cream, a chocolate Cream and butter curls). <span class="price">36</span></p>
    <p class="item"><span class="item-name">Cheese Croissant</span>Crumbly freshly baked with cheese filling. <span class="price">29</span></p>
    <p class="item"><span class="item-name">Daily Fresh Eggs</span>A choice of poached, scrambled, pan fried, omelet) all served with toasted Bread, mushrooms, roasted tomatoes and chicken sausages. <span class="price">59</span></p>
    <p class="item"><span class="item-name">Healthy Time</span>One choice of hot beverage from our cafe served with fruit salad, natural Yoghurt, whole wheat bread vegetable sandwiches and sugar free biscuits selection.<span class="price">49</span></p>
    <p class="item"><span class="item-name">Energy Time</span>One choice of hot beverage from our cafe served with finger chocolate muffins, Poached egg with toasted bread and crispy beef bacon, crepe roll with goat Cheese and honey and finger chocolate cream with salted cookies. <span class="price">59</span></p>
    <p class="item"><span class="item-name">Quill Vale Time</span>One choice of hot beverage from our cafe served with our selection of scones, Smoked salmon and avocado sandwich, roasted sausages sandwich, grilled vegetables sandwich, selection of our best biscuits. <span class="price">59</span></p>
    <p class="item"><span class="item-name">The Arabic Breakfast</span>Choice of Zattar Manakish and Cheese Manakish, served with one choice of hot beverage from our cafe and fresh orange juice. <span class="price">59</span></p>
  </div>
  <div class="column col-b">
    <h2>The Sandwiches</h2>
    <p class="item"><span class="inline-name">Grilled Vegetables Sandwich</span> with fresh Goat cheese and chives served with our Homemade spicy garlic mayo. <span class="price">59</span></p>
    <p class="item"><span class="inline-name">Butterfish burger</span> with fresh tomato, beef bacon, grilled vegetables and béarnaise sauce.</p>
    <p class="item"><span class="inline-name">Tataki Tuna sandwich</span> with red onion slices, stewed endives and black olives and sultanas pate'. <span class="price">79</span></p>
    <p class="item"><span class="inline-name">Beef sirloin</span> steak sandwich with grain mustard, Parmesan cheese and fresh Nashi pears. <span class="price">79</span></p>
    <p class="item"><span class="inline-name">The Traditional Club</span> sandwich served with French fries and vegetable chips. <span class="price">69</span></p>
    <p class="item"><span class="inline-name">Chicken sandwich</span> with Parmesan cheese slices, sundried tomatoes and mint Flavored mayo. <span class="price">69</span></p>
    <h2 class="later">Soup</h2>
    <p class="item"><span class="item-name">Bouillabaisse</span>Traditional French Seafood soup, with Saffron and Estragon. <span class="price">119</span></p>
    <p class="item"><span class="item-name">Barley soup</span>With fresh vegetables, tomato smoothie and a hint of garlic oil. <span class="price">49</span></p>
    <p class="item"><span class="item-name">Beef chili</span>Served with Arabic bread, fresh guacamole and spicy black beans. <span class="price">49</span></p>
  </div>
  <div class="photo photo-right ph-sandwich" role="img" aria-label="Photo of a baguette sandwich with tomato and lettuce"></div>
</section>

<section class="spread spread-two">
  <div class="photo photo-left ph-salad" role="img" aria-label="Photo of a spinach salad with strawberries and avocado"></div>
  <div class="column col-a">
    <h2>Salads</h2>
    <p class="item"><span class="item-name">Vegetarian Salad</span>Fresh green leaves, Italian cherry tomatoes, carrots, cucumber, green apple and toasted pine nuts with our special grain mustard dressing.<span class="price">59</span></p>
    <p class="item"><span class="item-name">Sweet Gorgonzola Cheese Salad</span>Fresh green leaves, Gorgonzola cheese, fresh pears, walnuts, garlic bread croutons, green celery with smoked honey dressing.<span class="price">59</span></p>
    <p class="item"><span class="item-name">Beef Sirloin Salad</span>Fresh green leaves, beef sirloin julienne, caramelized apples, Parmesan cheese, toasted almonds, sundried tomatoes and light Pesto sauce.<span class="price">79</span></p>
    <p class="item"><span class="item-name">Tandoori Chicken Salad</span>Fresh green leaves, Tandoori chicken breast, fresh mango, fresh goat cheese, crispy chicken skin and Jasmine rice sauce.<span class="price">69</span></p>
    <p class="item"><span class="item-name">Sea food Salad</span>Fresh green leaves, fresh steamed seafood, black olives, celery, garlic bread croutons, avocado and grapefruit dressing.<span class="price">89</span></p>
    <p class="item"><span class="item-name">Fresh Tuna Salad</span>Fresh green leaves, low temperature cooked tuna, taggiasca olives, red onions, roasted peppers, soy marinated tofu and lemon dressing.<span class="price">89</span></p>
  </div>
  <div class="column col-b">
    <h2>Appetizers</h2>
    <p class="item">with fresh Goat cheese and chives served with our Homemade spicy garlic mayo. <span class="price">59</span></p>
    <p class="item"><span class="inline-name">Butterfish burger</span> with fresh tomato, beef bacon, grilled vegetables and béarnaise sauce.</p>
    <p class="item"><span class="inline-name">Tataki Tuna sandwich</span> with red onion slices, stewed endives and black olives and sultanas pate'. <span class="price">79</span></p>
    <p class="item"><span class="inline-name">Beef sirloin</span> steak sandwich with grain mustard, Parmesan cheese and fresh Nashi pears. <span class="price">79</span></p>
    <p class="item"><span class="inline-name">The Traditional Club</span> served with French fries and vegetable chips. <span class="price">69</span></p>
    <p class="item"><span class="inline-name">Chicken sandwich</span> with Parmesan cheese slices, sundried tomatoes and mint Flavored mayo. <span class="price">69</span></p>
    <h2 class="later">Soup</h2>
    <p class="item"><span class="item-name">Bouillabaisse</span>Traditional French Seafood soup, with Saffron and Estragon. <span class="price">119</span></p>
    <p class="item"><span class="item-name">Barley soup</span>With fresh vegetables, tomato smoothie and a hint of garlic oil. <span class="price">49</span></p>
    <p class="item"><span class="item-name">Beef chili</span>Served with Arabic bread, fresh guacamole and spicy black beans. <span class="price">49</span></p>
  </div>
  <div class="photo photo-right ph-club" role="img" aria-label="Photo of stacked club sandwich halves with tomato and lettuce"></div>
</section>

</body>
</html>
```